Washing powder bag design.

Project Description – Graphic Design Proposal for ORNE Laundry Powder Packaging
We have already explored initial design ideas internally, supported by AI-assisted tools (ChatGPT) to develop early concepts, layouts, and mockups. To support this, we have attached the bag die-cut, where graphics and text are placed as a visual guideline for the intended structure. In addition, we have included a mockup of the product series currently under development to clearly communicate the desired style, direction, and overall visual identity.
The mockup should be regarded as the design foundation for this project and as a starting point for professional refinement.
Scope of Work
We would like you to create three graphic design variants, each based on a different color direction:
1. Variant 1: In line with our current color scheme
2. Variant 2: A blue version
3. Variant 3: A green version
Design Elements to Be Preserved
The following elements must be maintained across all three variants:
• The overall style and visual expression of the mockup
• The leaf-shaped element in the bottom right corner
• The ORNE layout, including typography, positioning, and general look & feel
Summary
While the color palette may vary, the structure, style, and key design elements must remain consistent and be directly based on the attached mockup.
We look forward to seeing your creative interpretation and professional input.
Updates
We need the design to be created based on the attached die-cut file “Orne 10 kg BAG 202526”, including all text elements.
We would like the final to include both the designed die-cut file and a mockup.

```html
<!DOCTYPE html>
<html lang="da">
<head>
<meta charset="utf-8">
<title>ORNE Vaskepulver 10 kg – front panel</title>
<link rel="stylesheet" href="https://fonts.googleapis.com/css2?family=Crimson+Text:wght@400;600&display=swap">
<style>
  :root {
    --page-bg: #ffffff;
    --bag-cream: #f4eedf;
    --forest-green: #3d5e4b;
    --sage-light: #c9d7b6;
    --leaf-tone: #6f8a76;
    --ink-green: #2f4a3b;
    --hole-white: #ffffff;
  }
  html, body {
    margin: 0;
    padding: 0;
    width: 1200px;
    height: 1039px;
    overflow: hidden;
    background: var(--page-bg);
  }
  .canvas {
    position: relative;
    width: 1200px;
    height: 1039px;
  }
  .front-panel {
    position: absolute;
    left: 370px;
    top: 40px;
    width: 460px;
    height: 960px;
    background: var(--bag-cream);
    overflow: hidden;
    font-family: "Crimson Text", Georgia, serif;
  }
  .hang-hole {
    position: absolute;
    top: 35px;
    width: 28px;
    height: 28px;
    border-radius: 50%;
    background: var(--hole-white);
  }
  .hang-hole--1 { left: 146px; }
  .hang-hole--2 { left: 209px; }
  .hang-hole--3 { left: 272px; }

  .tagline-arc {
    position: absolute;
    left: 80px;
    top: 90px;
    width: 320px;
    height: 120px;
  }
  .tagline-arc text {
    font-family: "Crimson Text", Georgia, serif;
    font-size: 15px;
    letter-spacing: 1.2px;
    fill: var(--ink-green);
  }

  .leaf-sprig {
    position: absolute;
    border-radius: 50% 40% 55% 45%;
  }
  .leaf-sprig--top {
    left: -10px;
    top: 134px;
    width: 266px;
    height: 335px;
    background: radial-gradient(ellipse at 45% 45%, rgba(111,138,118,0.35), rgba(111,138,118,0.08) 70%, transparent 80%);
  }
  .leaf-sprig--bottom {
    left: 128px;
    top: 666px;
    width: 340px;
    height: 300px;
    background: radial-gradient(ellipse at 50% 50%, rgba(111,138,118,0.35), rgba(111,138,118,0.08) 70%, transparent 80%);
  }

  .brand-badge {
    position: absolute;
    left: 256px;
    top: 193px;
    width: 158px;
    height: 158px;
    border-radius: 50%;
    background: var(--sage-light);
    display: flex;
    align-items: center;
    justify-content: center;
  }
  .brand-name {
    font-size: 46px;
    font-weight: 600;
    color: var(--forest-green);
    letter-spacing: 1px;
  }

  .product-disc {
    position: absolute;
    left: 29px;
    top: 341px;
    width: 414px;
    height: 414px;
    border-radius: 50%;
    background: var(--forest-green);
  }
  .product-title {
    position: absolute;
    left: 0;
    width: 460px;
    text-align: center;
    color: var(--bag-cream);
    margin: 0;
    font-weight: 400;
  }
  .product-title--da {
    top: 512px;
    font-size: 55px;
    line-height: 60px;
  }
  .product-title--en {
    top: 574px;
    font-size: 31px;
    line-height: 36px;
  }
  .net-weight {
    position: absolute;
    left: 40px;
    top: 878px;
    margin: 0;
    font-size: 28px;
    font-weight: 600;
    color: var(--ink-green);
  }
</style>
</head>
<body>
<main class="canvas">
  <section class="front-panel" aria-label="ORNE laundry powder bag, front">
    <span class="hang-hole hang-hole--1"></span>
    <span class="hang-hole hang-hole--2"></span>
    <span class="hang-hole hang-hole--3"></span>

    <svg class="tagline-arc" viewBox="0 0 320 120" aria-label="Liv og balance i hverdagen">
      <defs>
        <path id="tagline-curve" d="M 40 85 Q 160 0 290 85"/>
      </defs>
      <text><textPath href="#tagline-curve" startOffset="50%" text-anchor="middle">LIV OG BALANCE I HVERDAGEN</textPath></text>
    </svg>

    <div class="leaf-sprig leaf-sprig--top" role="img" aria-label="Line-drawn green leafy branch illustration"></div>

    <div class="brand-badge">
      <span class="brand-name">ORNE</span>
    </div>

    <div class="product-disc"></div>
    <h1 class="product-title product-title--da">VASKEPULVER</h1>
    <p class="product-title product-title--en">LAUNDRY DETERGENT</p>

    <div class="leaf-sprig leaf-sprig--bottom" role="img" aria-label="Line-drawn green leafy branch illustration in the bottom right corner"></div>

    <p class="net-weight">10kg</p>
  </section>
</main>
</body>
</html>
```